Package design for a set of baby wood brush

It has to be different from the competitions - here are the competitions, the box is the same size and shape, but I want the design to be different then others and stick out, yet to be suitable as baby product and baby shower gift.
I am going to call it "a soft sunny nap" it will be printed on the brush itself.
1) https://www.shopvellor.com/PIMLIkids-Newborns-Toddlers-Bristles-Registry/dp/K72QEX8N3T/ref=sr_1_7_a_it?ie=UTF8&qid=1496863496&sr=8-7&keywords=baby+brush
2) https://www.shopvellor.com/Newborns-Toddlers-Natural-Bristles-Registry/dp/K58TRUVZPM/ref=sr_1_17_a_it?ie=UTF8&qid=1496863576&sr=8-17&keywords=baby+brush
3) https://www.shopvellor.com/TotsMerva-Silicone-Newborns-Toddlers-Bristles/dp/K39FHQ24RN/ref=sr_1_21_a_it?ie=UTF8&qid=1496944927&sr=8-21&keywords=baby+wood+brush
The desighn should be different then the competitors but still transmit a natural baby product. there will also be a little text and a naturlality symbols.
Thanks

```html
<!DOCTYPE html>
<html lang="en">
<head>
<meta charset="utf-8">
<title>A Soft Sunny Nap – Baby Brush Box Dieline</title>
<link href="https://fonts.googleapis.com/css2?family=PT+Sans:ital,wght@0,400;0,700;1,700&family=Questrial&display=swap" rel="stylesheet">
<style>
  :root {
    --paper: #ffffff;
    --kraft: #d4b283;
    --kraft-edge: #c9a676;
    --line: #333333;
    --maroon: #94303a;
    --body-ink: #3b3434;
    --dim-grey: #a6a6a6;
    --side-label: #c2449a;
    --sun: #f5c52a;
    --icon-a: #f3a0c4;
    --icon-b: #6ccbd1;
    --icon-c: #f7d36a;
  }
  * { box-sizing: border-box; margin: 0; padding: 0; }
  html, body { width: 805px; height: 1200px; overflow: hidden; background: var(--paper); }
  .canvas { position: relative; width: 805px; height: 1200px; }

  .panel { position: absolute; border: 1px solid var(--line); }
  .panel.glue { background: var(--paper); }
  .panel.kraft { background: var(--kraft); }

  .flap-top { left: 250px; top: 0; width: 341px; height: 59px; }
  .lid-top { left: 250px; top: 58px; width: 341px; height: 151px; }
  .glue-left { left: 42px; top: 208px; width: 59px; height: 739px; }
  .side-left { left: 100px; top: 208px; width: 151px; height: 739px; }
  .front { left: 250px; top: 208px; width: 341px; height: 739px; }
  .side-right { left: 590px; top: 208px; width: 149px; height: 739px; }
  .glue-right { left: 738px; top: 208px; width: 60px; height: 739px; }
  .lid-bottom { left: 250px; top: 946px; width: 341px; height: 151px; }
  .flap-bottom { left: 250px; top: 1096px; width: 341px; height: 59px; }

  .wordmark {
    position: absolute; left: 0; right: 0;
    display: flex; align-items: center; justify-content: center; gap: 8px;
    font-family: "PT Sans", sans-serif; font-weight: 700;
    color: var(--maroon); letter-spacing: 0.5px;
  }
  .wordmark .sun-dot { width: 18px; height: 18px; border-radius: 50%; background: var(--maroon); flex: none; }
  .lid-top .wordmark { top: 52px; font-size: 28px; transform: rotate(180deg); }
  .lid-bottom .wordmark { top: 52px; font-size: 28px; }
  .front .wordmark { top: 162px; font-size: 34px; }
  .front .wordmark .sun-dot { width: 26px; height: 26px; background: var(--sun); }

  .icon-row { position: absolute; left: 50px; width: 240px; height: 34px; border-radius: 6px;
    background: linear-gradient(90deg, var(--icon-c), var(--icon-a), var(--icon-b), var(--icon-a), var(--icon-c)); opacity: .75; }
  .icon-row.upper { top: 50px; }
  .icon-row.lower { top: 630px; }
  .stripe-band { position: absolute; left: 0; width: 339px; height: 7px;
    background: linear-gradient(90deg, #a6dfe6, #f6b7cf, #f7dd8a, #b7e0a7, #a6dfe6); }
  .stripe-band.upper { top: 89px; }
  .stripe-band.lower { top: 664px; }

  .product-title {
    position: absolute; top: 246px; left: 0; right: 0; text-align: center;
    font-family: "PT Sans", sans-serif; font-style: italic; font-weight: 700;
    font-size: 19px; line-height: 27px; color: var(--maroon);
  }
  .benefits {
    position: absolute; top: 336px; left: 20px; right: 20px; text-align: center;
    font-family: "Questrial", sans-serif; font-size: 10.6px; line-height: 15px; color: var(--body-ink);
  }
  .benefits p + p { margin-top: 14px; }
  .bonus-label {
    position: absolute; top: 557px; left: 0; right: 0; text-align: center;
    font-family: "PT Sans", sans-serif; font-weight: 700; font-size: 11px; color: var(--maroon);
  }
  .bonus-label span { border-bottom: 1px solid var(--maroon); padding-bottom: 1px; }
  .bonus-text {
    position: absolute; top: 575px; left: 10px; right: 10px; text-align: center;
    font-family: "Questrial", sans-serif; font-size: 10.6px; line-height: 15px; color: var(--body-ink);
  }
  .bonus-text strong { font-family: "PT Sans", sans-serif; font-weight: 700; }

  .dimension { position: absolute; font-family: "PT Sans", sans-serif; font-size: 28px; color: var(--dim-grey); }
  .dim-lid-top { left: 609px; top: 117px; }
  .dim-height { left: -18px; top: 562px; transform: rotate(-90deg); }
  .dim-lid-bottom { left: 618px; top: 970px; }
  .dim-flap { left: 148px; top: 1108px; }
  .dim-width { left: 381px; top: 1162px; }
  .side-label { position: absolute; left: 627px; top: 1112px; font-family: "PT Sans", sans-serif; font-size: 46px; color: var(--side-label); }
</style>
</head>
<body>
<main class="canvas">
  <div class="panel glue flap-top"></div>
  <section class="panel kraft lid-top">
    <div class="wordmark"><span class="sun-dot"></span>A Soft Sunny Nap</div>
  </section>

  <div class="panel glue glue-left"></div>
  <div class="panel kraft side-left"></div>

  <section class="panel kraft front">
    <div class="icon-row upper" role="img" aria-label="Row of small baby-themed icons: mirror, goat, puppy, brush, gift, comb, chick"></div>
    <div class="stripe-band upper" role="img" aria-label="Pastel striped band"></div>

    <div class="wordmark"><span class="sun-dot"></span>A Soft Sunny Nap</div>

    <h1 class="product-title">Baby Wooden Hair Brush Set<br>Natural Eco Friendly<br>3 Piece Set</h1>

    <div class="benefits">
      <p>The silky soft hair bristles are gentle for the<br>sensitive scalps of newborn and toddlers.</p>
      <p>All natural beech wood bristles stimulate<br>the scalp and increase circulation while<br>relaxing your baby.</p>
      <p>100% goat hair and wooden bristles<br>condition baby's hair and evenly distributes<br>natural oils down the shaft.</p>
      <p>Premium wooden comb perfect for<br>sectioning hair and great for cradle cap.</p>
    </div>

    <div class="bonus-label"><span>Bonus inside</span></div>
    <p class="bonus-text">Baby Nail File. Made from tempered Czech<br>glass of the finest quality with smooth rounded ends,<br><strong>especially suitable for your baby.</strong></p>

    <div class="icon-row lower" role="img" aria-label="Row of small baby-themed icons: bear, brush, butterfly, teddy, sheep, mirror"></div>
    <div class="stripe-band lower" role="img" aria-label="Pastel striped band"></div>
  </section>

  <div class="panel kraft side-right"></div>
  <div class="panel glue glue-right"></div>

  <section class="panel kraft lid-bottom">
    <div class="wordmark"><span class="sun-dot"></span>A Soft Sunny Nap</div>
  </section>
  <div class="panel glue flap-bottom"></div>

  <span class="dimension dim-lid-top">38mm</span>
  <span class="dimension dim-height">189mm</span>
  <span class="dimension dim-lid-bottom">38mm</span>
  <span class="dimension dim-flap">15mm</span>
  <span class="dimension dim-width">87mm</span>
  <span class="side-label">Bottom</span>
</main>
</body>
</html>
```